Business card design needed for elearning/LMS consultant

I'm an elearning and learning management system (LMS) consultant that requires a minimalist, technology/cutting edge, business card. I do not have a logo or colour scheme. I offer clients hands on expertise in 'elearning authouring', 'LMS ecosystems', 'elearning strategy', 'technical implementation', 'mlearning', 'LMS evaluation', 'big data', 'learner analytics' and 'reporting strategy', 'social learning', 'elearning blueprint'. I'm thinking a 'tag cloud' of the above services on the back of the card, with contact details on front, but unsure if it's passe so please don't let it constrain you.

Target Market(s)

C-level executives, learning and development senior management,

Industry/Entity Type

Business

Contact Information for Business Card

Dorian Vastwick
dorian.vastwick@mailbrook.net
0417 362 958

Requirements
Should not have
• cheesy headshots, overused stockphotos, CLIPART and comic sans ;)

```html
<!DOCTYPE html>
<html lang="en">
<head>
<meta charset="utf-8">
<title>Dorian Vastwick – e-learning consultant</title>
<link rel="stylesheet" href="https://fonts.googleapis.com/css2?family=Poppins:wght@600&family=Questrial&display=swap">
<style>
  :root {
    --paper: #ffffff;
    --ink-grey: #58595b;
    --accent-blue: #0071bc;
    --accent-pink: #ec008c;
  }
  html, body {
    margin: 0;
    padding: 0;
    overflow: hidden;
    background: var(--paper);
  }
  .business-card {
    display: block;
    width: 1200px;
    height: 693px;
    background: var(--paper);
    overflow: hidden;
  }
  .display-letters {
    font-family: "Poppins", "Century Gothic", sans-serif;
    font-weight: 600;
  }
  .display-letters--blue { fill: var(--accent-blue); }
  .display-letters--pink { fill: var(--accent-pink); }
  .card-name {
    font-family: "Poppins", "Century Gothic", sans-serif;
    font-weight: 600;
    font-size: 78px;
    letter-spacing: -1px;
  }
  .card-name__first { fill: var(--ink-grey); }
  .card-name__last { fill: var(--accent-blue); }
  .card-role,
  .card-contact {
    font-family: "Questrial", "Century Gothic", sans-serif;
    fill: var(--ink-grey);
  }
  .card-role { font-size: 50px; }
  .card-contact { font-size: 38px; }
</style>
</head>
<body>
<svg class="business-card" viewBox="0 0 1200 693" xmlns="http://www.w3.org/2000/svg" role="img" aria-label="Business card for Dorian Vastwick, e-learning consultant">
  <rect width="1200" height="693" fill="var(--paper)"/>

  <text class="display-letters display-letters--blue" x="540" y="10" font-size="430" transform="rotate(31 540 10)">tw</text>
  <text class="display-letters display-letters--pink" x="-190" y="420" font-size="520" transform="rotate(31 -190 420)">ian</text>

  <text class="card-name" x="455" y="112" transform="rotate(31 455 112)"><tspan class="card-name__first">Dorian </tspan><tspan class="card-name__last">Vastwick</tspan></text>

  <text class="card-role" x="568" y="276" transform="rotate(31 568 276)">e-learning consultant</text>

  <text class="card-contact" x="136" y="108" transform="rotate(31 136 108)">e: dorian.vastwick@mailbrook.net</text>
  <text class="card-contact" x="92" y="196" transform="rotate(31 92 196)">t: 0417 362 958</text>
</svg>
</body>
</html>
```